Tatami Hall Sport promotional leaflet to attract new members

We are looking to produce a leaflet for a local judo club to attract seniors and juniors 5+ the leaflet needs to encourage people to attend classes and train in the martial art

Tatami Hall Sport are proud members of the KSB UK (mats for every) and practice traditional judo which mean we wear white Gi's to show cleanliness and tradition.

www.tatamihallsport.co.uk

Target Market(s)

Kids from 5+ and Adults

Font styles to use
Serif

Requirements
Must have
• Must include times of training and how to book onto a beginners induction
• it must look enticing and show that Judo is fun for all
• must highlight we open on Tuesdays and Thursdays
• Juniors are from 6.15pm to 7.15pm
• seniors 7.30pm to 9pm
• classes are held at Vantrel Gym, Unit 7, Marlow Row, Denholm Close, Rustington, West Sussex, BN17 8QT
• We practice on a Sprung floor Mat area and is great for men and women
• first two classes free
Nice to have
• Classes are run by an expeirnced team including
• Dan Merrow 5th Dan and international referee
• Luke Merrow 2nd Dan current Global Grappling Union European Champion

```html
<!DOCTYPE html>
<html lang="en">
<head>
<meta charset="utf-8">
<title>Tatami Hall Sport – Leaflet</title>
<link href="https://fonts.googleapis.com/css2?family=Montserrat:wght@400;500;600;700;800&display=swap" rel="stylesheet">
<style>
  :root {
    --red: #a3141f;
    --red-dark: #6e0f16;
    --ink: #232325;
    --ink-soft: #2f2f32;
    --paper: #ececec;
    --paper-white: #f7f7f7;
    --text-grey: #555558;
    --text-light: #cfcfcf;
    --stage: #dcdcdc;
  }
  * { box-sizing: border-box; margin: 0; padding: 0; }
  html, body { width: 1200px; height: 801px; overflow: hidden; }
  body {
    background: var(--stage);
    font-family: "Montserrat", sans-serif;
    position: relative;
  }
  .leaflet {
    position: absolute; left: 45px; top: 40px;
    width: 1110px; height: 720px;
    display: flex;
    box-shadow: 0 10px 30px rgba(0,0,0,.25);
  }
  .panel { position: relative; width: 370px; height: 720px; overflow: hidden; }
  .panel svg.shapes { position: absolute; inset: 0; }

  /* ---------- Training panel ---------- */
  .panel--training { background: var(--ink); color: var(--text-light); }
  .panel-title {
    position: absolute; left: 22px; top: 26px;
    font-size: 19px; font-weight: 700; color: #fff;
    padding: 3px 10px;
    background: linear-gradient(90deg, var(--red) 0%, var(--red-dark) 100%);
  }
  .session { position: absolute; width: 170px; font-size: 8.6px; line-height: 1.45; }
  .session h3 { font-size: 12.5px; font-weight: 700; color: #fff; text-transform: uppercase; margin-bottom: 6px; letter-spacing: .3px; }
  .tag {
    display: inline-block; background: var(--red); color: #fff;
    font-weight: 700; font-size: 8.6px; padding: 1px 6px; margin: 4px 0 2px;
  }
  .session p { margin-bottom: 3px; }
  .session .note { margin-top: 6px; color: #b9b9b9; }
  .session--tue { left: 22px; top: 80px; }
  .session--thu { left: 190px; top: 300px; }
  .session--venue { left: 22px; top: 500px; }

  /* ---------- About panel ---------- */
  .panel--about { background: var(--paper); color: var(--text-grey); }
  .about-title {
    position: absolute; left: 22px; top: 26px;
    font-size: 18px; font-weight: 700; color: var(--red);
    border-bottom: 5px solid var(--ink); padding-bottom: 2px;
  }
  .about-body {
    position: absolute; left: 24px; top: 70px; width: 320px;
    font-size: 8.8px; line-height: 1.5;
  }
  .about-body p { margin-bottom: 12px; }
  .about-body strong { color: var(--ink); text-transform: uppercase; }
  .about-body ul { margin: 0 0 12px 26px; }
  .about-body li { margin-bottom: 1px; }
  .contact { position: absolute; left: 24px; top: 545px; width: 320px; }
  .contact h2 { font-size: 21px; font-weight: 700; color: var(--red); margin-bottom: 4px; }
  .contact .phone { font-size: 18px; font-weight: 600; color: var(--ink); margin-left: 34px; margin-bottom: 6px; }
  .contact-line { display: flex; align-items: center; gap: 8px; font-size: 9px; margin: 5px 0 0 34px; }
  .contact-line svg { width: 14px; height: 14px; flex: none; }

  /* ---------- Cover panel ---------- */
  .panel--cover { background: var(--paper-white); }
  .brand {
    position: absolute; left: 0; right: 0; top: 440px;
    display: flex; align-items: center; justify-content: center; gap: 8px;
  }
  .brand-dot { width: 20px; height: 20px; border-radius: 50%; background: var(--red); }
  .brand-name { font-size: 18px; font-weight: 500; color: var(--ink); text-transform: uppercase; letter-spacing: .5px; }
  .tagline { position: absolute; right: 28px; top: 510px; text-align: right; color: var(--ink); }
  .tagline .lead { font-size: 15px; font-weight: 500; }
  .tagline .big { font-size: 30px; font-weight: 800; color: var(--red); line-height: 1.05; letter-spacing: 1px; }
  .tagline .small { font-size: 14px; font-weight: 600; }
</style>
</head>
<body>
<main class="leaflet">

  <!-- Training times and venue -->
  <section class="panel panel--training">
    <svg class="shapes" viewBox="0 0 370 720" aria-hidden="false">
      <defs>
        <linearGradient id="hallA" x1="0" y1="0" x2="1" y2="1">
          <stop offset="0" stop-color="#c9c6c2"/><stop offset=".6" stop-color="#8a6d6a"/><stop offset="1" stop-color="#7a1a22"/>
        </linearGradient>
        <linearGradient id="hallB" x1="0" y1="0" x2="1" y2="1">
          <stop offset="0" stop-color="#d8d6d2"/><stop offset="1" stop-color="#6b6a6c"/>
        </linearGradient>
        <linearGradient id="throwC" x1="0" y1="0" x2="1" y2="1">
          <stop offset="0" stop-color="#1d2a4a"/><stop offset=".6" stop-color="#3a4c7a"/><stop offset="1" stop-color="#e2e2e2"/>
        </linearGradient>
      </defs>
      <!-- Tuesday photo -->
      <polygon points="350,95 350,330 200,330" fill="none" stroke="#fff" stroke-width="3"/>
      <polygon points="345,110 345,324 212,324" fill="url(#hallA)" role="img" aria-label="Photo of juniors training on the red and blue mats"/>
      <polygon points="210,290 210,345 250,317" fill="var(--red-dark)"/>
      <!-- Thursday photo -->
      <polygon points="18,290 18,505 175,390" fill="none" stroke="#fff" stroke-width="3"/>
      <polygon points="22,300 22,495 165,392" fill="url(#hallB)" role="img" aria-label="Photo of judoka in white gi practising a hold"/>
      <polygon points="130,370 175,370 152,410" fill="var(--red-dark)"/>
      <!-- Venue photo -->
      <polygon points="330,520 330,690 210,610" fill="url(#throwC)" role="img" aria-label="Photo of two judoka performing a throw"/>
      <polygon points="190,560 240,600 200,640" fill="var(--red)"/>
      <polygon points="200,600 240,640 205,680" fill="none" stroke="#fff" stroke-width="2"/>
      <!-- bottom chevrons -->
      <polygon points="0,720 60,640 130,720" fill="var(--red-dark)"/>
      <polygon points="40,720 100,670 160,720" fill="#3a3a3d"/>
    </svg>

    <h2 class="panel-title">Training Times and Venue:</h2>

    <div class="session session--tue">
      <h3>Tuesday Training</h3>
      <span class="tag">Juniors:</span>
      <p>(5 to 15 years old) 6.15pm to 7.15pm</p>
      <span class="tag">Seniors:</span>
      <p>(16+ unless invited) 7.30pm to 9pm</p>
      <p class="note">Tuesday will be the first session of the week, before the session you will know what we will be working on. Normally we will focus on what is coming up in the future i.e. gradings or competitions.</p>
    </div>

    <div class="session session--thu">
      <h3>Thursday Training</h3>
      <span class="tag">Juniors:</span>
      <p>(5 to 15 years old) 6.15pm to 7.15pm</p>
      <span class="tag">Seniors:</span>
      <p>(16+ unless invited) 7.30pm to 9pm</p>
      <p class="note">Our second training day in Worthing, we will look to take what we have learnt and progress this. Similarly to Tuesday we will continue developing our Judo which will include practising techniques and Randori (free practice fighting).</p>
    </div>

    <div class="session session--venue">
      <span class="tag">Venue:</span>
      <h3 style="margin-top:6px">Our Training Venue</h3>
      <p class="note">All of our judo training sessions are held at our dojo inside Vantrel Gym, Rustington. Our new Dojo boasts a 132 square metre sprung floor; the sprung floor is not only comfortable to train on but is essential for shock absorption in our training sessions. We're extremely excited to have this feature and we hope you enjoy it as much as we do.</p>
    </div>
  </section>

  <!-- About and contact -->
  <section class="panel panel--about">
    <svg class="shapes" viewBox="0 0 370 720" aria-hidden="true">
      <polygon points="0,0 60,0 0,70" fill="#dcdcdc"/>
      <polygon points="300,720 370,640 370,720" fill="#d6d6d6"/>
    </svg>
    <h2 class="about-title">About Tatami Hall Sport:</h2>
    <div class="about-body">
      <p><strong>It all started when</strong> Tatami Hall Sport was formed in 2018 upon the vision of building a club based on hard work, technical ability and celebration of success. Our members are the heart of our club; we aim to work with our members individually to support them in their training and to understand their personal goals, whether that is in theory, competition, fitness or simply to build confidence.</p>
      <p>We work to actively reinvest in our members by making all of our events affordable in the promise of giving every member the opportunity to take part and subsequently progress in their Judo. Some of our events include Randori sessions, National competitions, tailored training packages and great social events! Tatami Hall Sport is one of a handful of clubs recognised by KSB UK (mats for every). As the national governing body for traditional Judo in the UK, this means we can provide access to lots of unique opportunities, including having the KSB UK president Sensei Harlow at the helm of our organisation, supporting our teaching, practice and development of traditional Judo.</p>
      <p>These opportunities are available with the expectation that all of our members will:</p>
      <ul>
        <li>Demonstrate the desire to want to participate.</li>
        <li>Commit to regular training (twice a week).</li>
        <li>Give 100% every session.</li>
        <li>Represent the club with the appropriate etiquette.</li>
      </ul>
      <p>Although we require you to work hard, we also want you to have fun and get the most out of your sessions. Being a part of a team means celebrating your successes and supporting you in your failures.</p>
      <p>If in doubt give Judo a try, your first two sessions are free – you have nothing to lose!</p>
    </div>

    <div class="contact">
      <h2>Contact Details:</h2>
      <p class="phone">+01632 960418</p>
      <p class="contact-line">
        <svg viewBox="0 0 14 14" aria-hidden="true"><path d="M7 1a4 4 0 0 0-4 4c0 3 4 8 4 8s4-5 4-8a4 4 0 0 0-4-4zm0 5.5A1.5 1.5 0 1 1 7 3.5a1.5 1.5 0 0 1 0 3z" fill="#666"/></svg>
        Marlow Row - Rustington | BN17 8QT | UK
      </p>
      <p class="contact-line">
        <svg viewBox="0 0 14 14" aria-hidden="true"><circle cx="7" cy="7" r="6" fill="none" stroke="#666" stroke-width="1.3"/><path d="M4.5 4.5c.5 2.5 2.5 4.5 5 5l.8-1-1.5-1-.7.6c-.9-.5-1.6-1.2-2.1-2.1l.6-.7-1-1.5z" fill="#666"/></svg>
        Aled Corran | +01632 960418
      </p>
      <p class="contact-line">
        <svg viewBox="0 0 14 14" aria-hidden="true"><circle cx="7" cy="7" r="6" fill="none" stroke="#666" stroke-width="1.3"/><rect x="4" y="5" width="6" height="4.2" fill="none" stroke="#666" stroke-width="1"/><path d="M4 5l3 2.3L10 5" fill="none" stroke="#666" stroke-width="1"/></svg>
        hello@tatamihallsport.co.uk
      </p>
    </div>
  </section>

  <!-- Cover -->
  <section class="panel panel--cover">
    <svg class="shapes" viewBox="0 0 370 720" aria-hidden="false">
      <defs>
        <linearGradient id="groupD" x1="0" y1="0" x2="1" y2="1">
          <stop offset="0" stop-color="#4a4a50"/><stop offset=".5" stop-color="#b8b6b4"/><stop offset="1" stop-color="#e6e4e2"/>
        </linearGradient>
      </defs>
      <rect x="0" y="0" width="370" height="150" fill="url(#groupD)" role="img" aria-label="Group photo of club members in white gi lined up in the dojo"/>
      <polygon points="0,0 90,0 0,110" fill="var(--red-dark)"/>
      <polygon points="0,110 90,0 150,0 30,180 0,180" fill="#f7f7f7"/>
      <polygon points="370,150 370,210 250,150" fill="#f7f7f7"/>
      <polygon points="0,180 0,150 200,150 370,150 370,160 0,250" fill="#f7f7f7"/>
      <polygon points="120,150 190,95 260,150" fill="var(--red)"/>
      <polygon points="60,180 100,150 100,200" fill="var(--ink)"/>
      <polygon points="185,170 290,280 185,390 80,280" fill="none" stroke="var(--red)" stroke-width="6"/>
      <polygon points="185,205 255,280 185,355 115,280" fill="var(--red)"/>
      <polygon points="290,210 330,250 290,290" fill="var(--red-dark)"/>
      <polygon points="60,330 100,370 60,400" fill="#c9c9c9"/>
      <polygon points="320,540 335,555 320,570" fill="#c9c9c9"/>
      <polygon points="335,600 350,615 335,630" fill="var(--red-dark)"/>
      <!-- bottom chevrons -->
      <polygon points="0,720 95,630 190,720" fill="var(--red)"/>
      <polygon points="30,720 95,665 160,720" fill="#f7f7f7"/>
      <polygon points="55,720 95,690 135,720" fill="var(--ink)"/>
      <polygon points="190,720 370,650 370,720" fill="#e2e2e2"/>
    </svg>

    <div class="brand">
      <span class="brand-dot"></span>
      <span class="brand-name">Tatami Hall Sport</span>
    </div>

    <div class="tagline">
      <p class="lead">A club setup by</p>
      <p class="big">JUDOKAS</p>
      <p class="small">for Judokas.</p>
    </div>
  </section>

</main>
</body>
</html>
```